Website for Hargreave Fabrication & Construction Ltd

General Note to all.

1. Piling and gas works are separate areas of work and should not be put together.
- the marine section should really be the piling works and should have all the barges/water piles etc.
- the gas section should have the big silo looking thing

2. I would like to add in Specialist Onsite Labour and Management in the 'our services' section. The would include the Supervisors, Coded Welders, Site Fitters and Crane and Rig Crews etc.

3. I did like it how someone had use the HFC header logo as the top of the webpage with the individual tabs above and the website starting below. Please remove the VAT number and phone number from this section.

4. I also liked how one designer incorporate the orange line with spark (from the logo) as a page separator representing the welding part of the business

5. Add in a Mission Statement - To go above and beyond in to ensure our clients projects are delivered safely, ahead of schedule, in any environment for the benefit of not only our customers but also our employees and communities we work in.

6. Add in Business Objectives -HFC is on a mission to be one of the leading contractors in UK to supply All Site Labour - ranging from Site Management, fully Coded Welders, Site Fitters and Crane and Rig Crews.

7. I am happy for you to add in photos that are not ours for the thumbs nails for the our services. ie a colourful welding pics/cool tunnelling pic etc - just make sure I will not get done for copy write infringements

8. I would like a some type of 'contact us' field or 'request a consultation' section.

9. Please confirm if the webpages you create will be compatible for both desktop and mobile app and how difficult it will be to update personally once it is live.

10. You have all done very well and have thus far been very impressed with what you have produced. I gave a very vague brief as I was not entirely sure how you would go about making something with very little information. Some of the designs look very professional.

11. I'm not sure how once I choose the winning design how that then transfers over to my domain? Perhaps someone can help me with that? I will also be looking for a web hosting platform so feel free to provide this information.

After using Sketch hive for successful getting a professional logo for the company I'm giving the web design option a go.

I am looking for a professional website for the above civil construction company.

The company director has many years experience in Marine, tunnelling, conveyors, stadium construction gas and piling works including piling works for coal ports, bridges and tunnels.

The company currently provide 20+ skilled and experienced guys from all trades (supervisors, coded welders, fitters, crane drivers and crane supervisors, rigglers, slingers and piling operatives) on the Wenlow Causeway project in London - London's new super sewer. Most of this work is off barges carrying cranes (upto 600T and drill rigs).

As we are looking to expand and get more subcontracts we need a web presence to say who we are and what we do.

I'll include the 2 company logos we currently use below

I have included an info doc with pics you may or may not use.

Target Market(s)

Mainly other large construction companies and potential subcontractors

Industry/Entity Type

Construction Company

Coding

Coded - Design and coding required

Font styles to use
Sans Serif

Colors
0655a3
f37122
ffffff

Requirements
Must have
• Few tabs
• Simple to use/update but still professional look
• The challenge will be making the website look professional with not much available content.
Should not have
• No residential house building

```html
<!DOCTYPE html>
<html lang="en">
<head>
<meta charset="utf-8">
<title>Hargreave Fabrication &amp; Construction</title>
<link href="https://fonts.googleapis.com/css2?family=Montserrat:wght@500;600;700&family=Roboto:wght@400;500;700&display=swap" rel="stylesheet">
<style>
:root{
  --blue:#0655a3;
  --blue-dark:#04468a;
  --orange:#f37122;
  --white:#ffffff;
  --ink:#333b44;
  --muted:#5c6670;
  --pale:#eef2f7;
  --tile:#dfe6ee;
  --footer:#1c2833;
  --footer-deep:#141d26;
}
*{box-sizing:border-box;margin:0;padding:0}
html,body{width:1200px;height:2799px;overflow:hidden}
body{position:relative;background:var(--white);font-family:'Roboto',Arial,sans-serif;color:var(--ink)}
.abs{position:absolute}
.heading{font-family:'Montserrat',Arial,sans-serif;font-weight:700}

/* header */
.topbar{left:0;top:0;width:1200px;height:116px;background:var(--blue)}
.badge{left:535px;top:0;width:130px;height:106px}
.badge-name{left:535px;top:30px;width:130px;text-align:center;font-family:'Montserrat',sans-serif;font-weight:700;font-size:30px;color:var(--blue)}
.nav{left:0;top:116px;width:1200px;height:41px;background:var(--orange);display:flex;padding-left:160px}
.nav a{font-family:'Montserrat',sans-serif;font-weight:600;font-size:10px;color:var(--white);text-decoration:none;display:flex;align-items:center;padding:0 18px;text-transform:uppercase}
.nav a.active{background:#d95d14}

/* hero */
.hero{left:0;top:157px;width:1200px;height:394px;background:linear-gradient(100deg,#2d3a44 0%,#5b6670 40%,#6f6a5e 65%,#3e4a52 100%)}
.hero-shade{left:0;top:157px;width:1200px;height:394px;background:rgba(10,20,30,.35)}
.hero-title{left:160px;top:268px;font-size:66px;color:var(--white);letter-spacing:1px;line-height:1}
.hero-sub{left:162px;top:338px;font-size:29px;color:var(--white);font-family:'Montserrat',sans-serif;font-weight:600;letter-spacing:.5px}
.btn-contact{left:160px;top:392px;width:183px;height:45px;background:var(--blue);color:var(--white);font-family:'Montserrat',sans-serif;font-weight:600;font-size:12px;display:flex;align-items:center;padding-left:32px;gap:40px}
.arrow-btn{width:30px;height:30px;background:var(--white);top:340px;display:flex;align-items:center;justify-content:center}

.consult{left:773px;top:231px;width:253px;height:295px;background:var(--white);box-shadow:0 2px 10px rgba(0,0,0,.25)}
.consult-head{left:761px;top:187px;width:277px;height:46px;background:var(--blue);color:var(--white);font-family:'Montserrat',sans-serif;font-weight:600;font-size:15px;display:flex;align-items:center;padding-left:20px;gap:14px}
.field{left:788px;width:224px;height:30px;background:#e8eef6;font-size:9.5px;color:var(--blue);padding:10px 12px}
.send{left:788px;top:466px;width:224px;height:35px;background:var(--orange);color:var(--white);font-family:'Montserrat',sans-serif;font-weight:600;font-size:10px;display:flex;align-items:center;justify-content:center}

/* works */
.work-box{top:603px;width:375px;height:237px;border:3px solid var(--blue);padding:50px 20px 0;text-align:center;font-size:10.5px;line-height:1.75;color:var(--muted)}
.work-box.gas{border-color:var(--orange)}
.work-box p+p{margin-top:18px}
.work-title{top:590px;background:var(--white);padding:0 12px;font-size:22px;color:var(--blue)}
.work-title.gas{color:var(--orange)}
.torch{left:560px;top:620px;width:80px;height:190px;border-radius:40px;background:radial-gradient(circle at 50% 80%,#f9a25a 0%,#f37122 18%,#6b85a8 40%,#ffffff 72%)}

/* services */
.services{left:0;top:886px;width:1200px;height:467px;background:var(--pale)}
.sec-title{width:1200px;left:0;text-align:center;font-size:25px;color:var(--blue)}
.sec-title span{color:var(--orange)}
.sec-rule{left:574px;width:52px;height:3px;background:var(--ink)}
.grid{left:160px;top:1004px;width:879px;height:298px;display:grid;grid-template-columns:repeat(4,1fr);grid-template-rows:repeat(2,1fr)}
.cell{background:var(--white);text-align:center;padding-top:26px}
.cell.alt{background:var(--tile)}
.cell svg{width:24px;height:24px}
.cell h3{font-family:'Montserrat',sans-serif;font-weight:600;font-size:10px;color:var(--ink);margin:10px 12px 6px;line-height:1.3;text-transform:uppercase}
.cell p{font-size:9.5px;line-height:1.7;color:var(--muted);padding:0 30px}

/* statements */
.statement{top:1405px;height:97px;border:1px solid #dfe4ea;padding:16px 20px}
.statement h2{font-size:22px;color:var(--blue);margin-bottom:10px}
.statement h2 span{color:var(--orange)}
.statement p{font-size:10px;line-height:1.9;color:var(--ink)}

/* our work */
.filters{left:160px;top:1672px;width:880px;display:flex;gap:17px;font-family:'Montserrat',sans-serif;font-weight:700;font-size:10.5px;color:var(--ink)}
.filters .on{color:var(--orange)}
.thumb{width:279px;height:180px}
.thumb-label{font-family:'Montserrat',sans-serif;font-weight:700;font-size:11px;color:var(--white);text-align:center}
.btn-all{left:508px;top:2142px;width:182px;height:43px;background:var(--orange);color:var(--white);font-family:'Montserrat',sans-serif;font-weight:600;font-size:10px;display:flex;align-items:center;padding-left:32px;gap:52px}

/* partners */
.partners{left:0;top:2232px;width:1200px;height:175px;background:var(--pale)}
.partner{top:2290px;height:62px;background:#c5cfd9}

/* footer */
.footer{left:0;top:2407px;width:1200px;height:327px;background:linear-gradient(180deg,#2a3844,#1a242e)}
.foot-bottom{left:0;top:2734px;width:1200px;height:65px;background:var(--footer-deep);color:#c8d0d8;font-size:10px;display:flex;align-items:center;justify-content:center}
.foot-h{top:2487px;font-family:'Montserrat',sans-serif;font-weight:700;font-size:17px;color:var(--white)}
.foot-txt{color:#d6dde4;font-size:10px;line-height:1.95}
.foot-txt b{color:var(--white)}
.foot-list{list-style:none;color:#d6dde4;font-size:10px;line-height:2.1}
.foot-list li::before{content:"\2192";margin-right:8px;color:var(--white)}
.contact-row{display:flex;gap:14px;align-items:flex-start;font-size:10px;color:#d6dde4;line-height:1.9;margin-bottom:16px}
.social{display:flex;gap:5px}
.social i{width:13px;height:13px;border-radius:50%;background:var(--white);display:block}
.read{color:var(--orange)}
</style>
</head>
<body>

<!-- header -->
<div class="abs topbar"></div>
<svg class="abs badge" viewBox="0 0 130 106" aria-hidden="true"><path d="M0 0H130V82L65 106 0 82Z" fill="#fff"/></svg>
<div class="abs badge-name">HFC</div>
<nav class="abs nav">
  <a class="active" href="#">Home</a><a href="#">Services</a><a href="#">About us</a><a href="#">Our work</a><a href="#">Contact</a>
</nav>

<!-- hero -->
<div class="abs hero" role="img" aria-label="Photo of crews working on a riverside piling site with barges and cranes"></div>
<div class="abs hero-shade"></div>
<h1 class="abs heading hero-title">HARGREAVE</h1>
<div class="abs hero-sub">FABRICATION &amp; CONSTRUCTIONS</div>
<div class="abs btn-contact">CONTACT US
  <svg width="20" height="14" viewBox="0 0 20 14"><rect x="0" y="0" width="20" height="14" fill="#fff"/><path d="M0 0l10 8 10-8" stroke="#0655a3" stroke-width="1.6" fill="none"/></svg>
</div>
<div class="abs arrow-btn" style="left:63px"><svg width="8" height="10" viewBox="0 0 8 10"><path d="M6 1L2 5l4 4" stroke="#333" stroke-width="1.6" fill="none"/></svg></div>
<div class="abs arrow-btn" style="left:1104px"><svg width="8" height="10" viewBox="0 0 8 10"><path d="M2 1l4 4-4 4" stroke="#333" stroke-width="1.6" fill="none"/></svg></div>

<div class="abs consult"></div>
<div class="abs consult-head">
  <svg width="20" height="18" viewBox="0 0 20 18"><path d="M0 8L20 0 15 18 9 12Z" fill="#fff"/></svg>
  REQUEST A CONSULTATION
</div>
<div class="abs field" style="top:257px">Full Name</div>
<div class="abs field" style="top:297px">Email Address</div>
<div class="abs field" style="top:335px">Phone Number</div>
<div class="abs field" style="top:373px;height:78px">Message</div>
<div class="abs send">SEND REQUEST</div>

<!-- piling and gas -->
<div class="abs work-box" style="left:160px">
  <p>Lorem ipsum dolor sit amet, consectetur adipiscing elit. Ut fermentum metus non gravida sollicitudin. Etiam vel dolor sollicitudin, fringilla erat sollicitudin, posuere quam. Vestibulum id euismod urna. Donec sed congue tortor. Cras enim est, efficitur ac dapibus quis, consequat vitae sapien. Duis luctus venenatis magna.</p>
  <p>Aliquam nisi libero, dapibus id metus quis, congue maximus lorem. Vivamus volutpat aliquam mi. In hac habitasse platea dictumst. Etiam ac lorem ut dolor luctus sagittis vel non felis.</p>
</div>
<h2 class="abs heading work-title" style="left:246px">PILING WORKS</h2>
<div class="abs work-box gas" style="left:664px">
  <p>Lorem ipsum dolor sit amet, consectetur adipiscing elit. Ut fermentum metus non gravida sollicitudin. Etiam vel dolor sollicitudin, fringilla erat sollicitudin, posuere quam. Vestibulum id euismod urna. Donec sed congue tortor. Cras enim est, efficitur ac dapibus quis, consequat vitae sapien. Duis luctus venenatis magna.</p>
  <p>Aliquam nisi libero, dapibus id metus quis, congue maximus lorem. Vivamus volutpat aliquam mi. In hac habitasse platea dictumst. Etiam ac lorem ut dolor luctus sagittis vel non felis.</p>
</div>
<h2 class="abs heading work-title gas" style="left:765px">GAS WORKS</h2>
<div class="abs torch" role="img" aria-label="Illustration of a welding torch throwing an orange spark"></div>

<!-- services -->
<div class="abs services"></div>
<h2 class="abs heading sec-title" style="top:928px">OUR <span>SERVICES</span></h2>
<div class="abs sec-rule" style="top:966px"></div>
<div class="abs grid">
  <div class="cell"><svg viewBox="0 0 24 24"><path d="M5 12a7 7 0 0 1 14 0H5zM4 12h16M12 15a4 4 0 0 1-4 4M12 15a4 4 0 0 0 4 4" stroke="#333" stroke-width="1.5" fill="none"/></svg><h3>Supervisors</h3><p>Lorem ipsum dolor sit amet, consectetur adipiscing elit.</p></div>
  <div class="cell alt"><svg viewBox="0 0 24 24"><path d="M3 3l14 14M17 17l4 4M17 17l-2 3" stroke="#333" stroke-width="1.5" fill="none"/></svg><h3>Coded Welders</h3><p>Lorem ipsum dolor sit amet, consectetur adipiscing elit.</p></div>
  <div class="cell"><svg viewBox="0 0 24 24"><circle cx="12" cy="7" r="4" stroke="#333" stroke-width="1.5" fill="none"/><path d="M4 22v-4a8 5 0 0 1 16 0v4z" stroke="#333" stroke-width="1.5" fill="none"/></svg><h3>Fitters</h3><p>Lorem ipsum dolor sit amet, consectetur adipiscing elit.</p></div>
  <div class="cell alt"><svg viewBox="0 0 24 24"><path d="M4 20h14v-4H4zM8 16l8-12M16 4v8" stroke="#333" stroke-width="1.5" fill="none"/></svg><h3>Crane Drivers</h3><p>Lorem ipsum dolor sit amet, consectetur adipiscing elit.</p></div>
  <div class="cell alt"><svg viewBox="0 0 24 24"><path d="M6 22V3h14M6 6h14M18 6v6M4 22h6" stroke="#333" stroke-width="1.5" fill="none"/></svg><h3>Crane Supervisors</h3><p>Lorem ipsum dolor sit amet, consectetur adipiscing elit.</p></div>
  <div class="cell"><svg viewBox="0 0 24 24"><rect x="4" y="9" width="16" height="8" stroke="#333" stroke-width="1.5" fill="none"/><circle cx="8" cy="19" r="2" fill="#333"/><circle cx="16" cy="19" r="2" fill="#333"/></svg><h3>Rigglers</h3><p>Lorem ipsum dolor sit amet, consectetur adipiscing elit.</p></div>
  <div class="cell alt"><svg viewBox="0 0 24 24"><path d="M3 10h18l-3 7H6zM9 10V6h6v4" stroke="#333" stroke-width="1.5" fill="none"/></svg><h3>Slingers and<br>Piling Operatives</h3><p>Lorem ipsum dolor sit amet, consectetur adipiscing elit.</p></div>
  <div class="cell"><svg viewBox="0 0 24 24"><path d="M4 20l8-16 8 16M8 13h8" stroke="#333" stroke-width="1.5" fill="none"/></svg><h3>Specialist Onsite<br>Labour and Management</h3><p>Lorem ipsum dolor sit amet, consectetur adipiscing elit.</p></div>
</div>

<!-- mission & objectives -->
<div class="abs statement" style="left:160px;width:428px">
  <h2 class="heading">MISSION <span>STATEMENT</span></h2>
  <p>To go above and beyond in to ensure our clients projects are delivered safely, ahead of schedule, in any environment for the benefit of not only our customers but also our employees and communities we work in</p>
</div>
<div class="abs statement" style="left:610px;width:429px">
  <h2 class="heading">BUSINESS <span>OBJECTIVES</span></h2>
  <p>HFC is on a mission to be one of the leading contractors in UK to supply All Site Labour - ranging from Site Management, fully Coded Welders, Site Fitters and Crane and Rig Crews.</p>
</div>

<!-- our work -->
<h2 class="abs heading sec-title" style="top:1600px">OUR WORK</h2>
<div class="abs sec-rule" style="top:1636px"></div>
<div class="abs filters">
  <span class="on">ALL PROJECTS</span><span>BUILDINGS</span><span>MARINE</span><span>TUNNELLING</span><span>CONVEYORS</span><span>STADIUM CONSTRUCTION GAS</span><span>PILING WORKS</span><span>BRIDGES AND TUNNELS</span>
</div>
<div class="abs thumb" style="left:160px;top:1715px;background:#e57a35" role="img" aria-label="Tunnelling project photo under an orange overlay"></div>
<svg class="abs" style="left:278px;top:1775px" width="42" height="42" viewBox="0 0 42 42" aria-hidden="true"><circle cx="21" cy="21" r="19" stroke="#fff" stroke-width="2" fill="none"/><path d="M16 26l10-10M18 14h10v10" stroke="#fff" stroke-width="2" fill="none"/></svg>
<div class="abs thumb-label" style="left:160px;top:1827px;width:279px">TUNNELING</div>
<div class="abs thumb" style="left:461px;top:1715px;background:linear-gradient(180deg,#8f9aa6 0%,#a4a9a8 45%,#6b6a5a 70%,#4a4a44 100%)" role="img" aria-label="Photo of a yellow piling barge on the river"></div>
<div class="abs thumb" style="left:761px;top:1715px;background:linear-gradient(160deg,#7c8388 0%,#b06a3a 45%,#5d5f5e 100%)" role="img" aria-label="Photo of crew in orange overalls on a boat"></div>
<div class="abs thumb" style="left:160px;top:1916px;background:linear-gradient(180deg,#8a9bac 0%,#c8c8c0 45%,#40474c 100%)" role="img" aria-label="Photo of crane barges at dusk"></div>
<div class="abs thumb" style="left:461px;top:1916px;background:linear-gradient(180deg,#a9b6c4 0%,#b95a55 50%,#53504a 100%)" role="img" aria-label="Photo of a red lattice crane on site"></div>
<div class="abs thumb" style="left:761px;top:1916px;background:linear-gradient(135deg,#3d2a2a 0%,#8c3a3f 45%,#d8a1c8 70%,#4a3032 100%)" role="img" aria-label="Photo of a welder at work with bright sparks"></div>
<div class="abs btn-all">SEE ALL WORKS
  <svg width="10" height="14" viewBox="0 0 10 14"><path d="M2 1l6 6-6 6" stroke="#fff" stroke-width="2" fill="none"/></svg>
</div>

<!-- partners -->
<div class="abs partners"></div>
<div class="abs partner" style="left:178px;width:64px" role="img" aria-label="Wenlow Causeway partner badge"></div>
<div class="abs partner" style="left:296px;width:78px" role="img" aria-label="Partner badge"></div>
<div class="abs partner" style="left:428px;width:118px;border-radius:50%" role="img" aria-label="Partner badge"></div>
<div class="abs partner" style="left:594px;width:100px;height:54px;top:2296px" role="img" aria-label="Partner badge"></div>
<div class="abs partner" style="left:760px;width:110px;height:34px;top:2305px" role="img" aria-label="Partner badge"></div>
<div class="abs partner" style="left:924px;width:100px;height:34px;top:2305px" role="img" aria-label="Partner badge"></div>

<!-- footer -->
<div class="abs footer" role="img" aria-label="Dim photo of a riverside construction site behind the footer"></div>
<div class="abs" style="left:160px;top:2490px;width:60px;height:48px;background:var(--white);display:flex;align-items:center;justify-content:center;font-family:'Montserrat',sans-serif;font-weight:700;font-size:17px;color:var(--blue)">HFC</div>
<div class="abs foot-txt" style="left:230px;top:2490px"><b>Company Reg No: 10482273</b><br><b>VAT Reg No: 402 7716 58</b></div>
<div class="abs foot-txt" style="left:160px;top:2550px;width:215px">Daniel Hargreave was born and raised in South East London. After finishing school he completed a Welding <span class="read">Read More</span></div>
<div class="abs social" style="left:160px;top:2614px"><i></i><i></i><i></i><i></i></div>

<div class="abs foot-h" style="left:414px">TWITTER FEED</div>
<div class="abs foot-txt" style="left:414px;top:2527px;width:208px"><b>@Lorem ipsum:</b> dolor sit amet, consectetur adipiscing elit. Ut fermentum metus non gravida sollicitudin.<br><br><b>@Lorem ipsum:</b> dolor sit amet, consectetur adipiscing elit. Ut fermentum metus non gravida sollicitudin.</div>

<div class="abs foot-h" style="left:662px">QUICK LINKS</div>
<ul class="abs foot-list" style="left:662px;top:2527px">
  <li>Supervisors</li><li>Coded Welders</li><li>Fitters</li><li>Crane Drivers</li><li>Crane Supervisors</li><li>Rigglers</li>
</ul>

<div class="abs foot-h" style="left:836px">GET IN TOUCH</div>
<div class="abs" style="left:836px;top:2527px;width:200px">
  <div class="contact-row"><svg width="12" height="10" viewBox="0 0 12 10"><rect x=".5" y=".5" width="11" height="9" stroke="#f37122" fill="none"/><path d="M.5 .5l5.5 5 5.5-5" stroke="#f37122" fill="none"/></svg>info@hfc-site.co.uk</div>
  <div class="contact-row"><svg width="12" height="12" viewBox="0 0 12 12"><path d="M2 1l3 1v3l-1 1a7 7 0 0 0 2 2l1-1h3l1 3-2 1C5 11 1 7 1 3z" stroke="#f37122" fill="none"/></svg>07700 900461</div>
  <div class="contact-row"><svg width="10" height="13" viewBox="0 0 10 13"><path d="M5 12S1 7 1 4.5a4 4 0 0 1 8 0C9 7 5 12 5 12z" stroke="#f37122" fill="none"/><circle cx="5" cy="4.5" r="1.3" fill="#f37122"/></svg><span>1234 Lorem Ipsum Sit,<br>Dolor Fermentum, 4567.</span></div>
</div>

<div class="abs foot-bottom">Copyright © 2018 Hargreave Fabrication &amp; Construction. All rights reserved.</div>

</body>
</html>
```